i need to create a product label for honey jars i will be selling locally in Louisiana. product name will be Ridgeway Amber. i would like the label to include a notation "not recommended for infants under 1yrs of age".
net weight will be 16oz. also notate it is 100% raw honey. design would include a scripted font for the name but hoping to include aspect of the "bayou" theme like spanish moss or cypress trees but also include something in the design about honey. if there are any requirements that must be listed on there for sale please include them. artwork needs to be masculine but not set on specific colors.

```html
<!DOCTYPE html>
<html lang="en">
<head>
<meta charset="UTF-8">
<title>Ridgeway Amber – Raw Honey Label Set</title>
<link rel="stylesheet" href="https://fonts.googleapis.com/css2?family=Lobster&family=Andika&family=Montserrat:wght@800&display=swap">
<style>
  :root {
    --page: #f4f1ea;
    --cream: #f2e5b3;
    --honey: #f7c233;
    --honey-deep: #eea21f;
    --honey-light: #fbd96a;
    --amber: #f2a12c;
    --amber-badge: #f5b550;
    --brown: #3a2a12;
    --olive: #a88a2c;
    --moss: #6f8b3c;
    --moss-dark: #4e6a2b;
    --bark: #7c6a3c;
  }
  * { margin: 0; padding: 0; box-sizing: border-box; }
  html, body { width: 1200px; height: 1200px; overflow: hidden; }
  body { background: var(--page); position: relative; }

  .front-label {
    position: absolute; left: 60px; top: 210px;
    width: 520px; height: 780px;
    background: var(--cream);
    overflow: hidden;
  }
  .honey-band { position: absolute; left: 0; width: 100%; height: 70px; }
  .honey-band--top { top: 0; }
  .honey-band--bottom { bottom: 0; }

  .tree-art {
    position: absolute; left: 190px; top: 80px;
    width: 320px; height: 640px;
    border-radius: 46% 46% 18% 18% / 34% 34% 10% 10%;
    background: linear-gradient(180deg, var(--moss) 0%, var(--moss-dark) 45%, #8c8a55 68%, var(--bark) 100%);
    opacity: 0.85;
  }

  .raw-badge { position: absolute; left: 26px; top: 80px; width: 120px; }
  .raw-badge__pct {
    font-family: "Lobster", cursive; color: var(--honey-deep);
    font-size: 26px; margin-left: 14px; line-height: 1;
  }
  .raw-badge__tag {
    margin-top: 4px; background: var(--honey-deep); border-radius: 10px;
    padding: 10px 6px; text-align: center;
    font-family: "Montserrat", sans-serif; font-weight: 800;
    font-size: 14px; color: var(--brown); letter-spacing: 0.3px;
  }

  .product-name {
    position: absolute; left: 10px; top: 350px; width: 520px;
    text-align: center;
    font-family: "Lobster", cursive; font-size: 66px;
    color: var(--amber); line-height: 1;
    transform: rotate(-16deg);
  }

  .infant-notice {
    position: absolute; left: 0; top: 612px;
    width: 210px; padding: 12px 14px 12px 22px;
    background: var(--amber-badge); border-radius: 0 16px 16px 0;
    font-family: "Andika", sans-serif; font-size: 15px;
    color: var(--brown); line-height: 1.3;
  }
  .net-weight {
    position: absolute; left: 40px; top: 690px;
    font-family: "Montserrat", sans-serif; font-weight: 800;
    font-size: 20px; color: var(--brown);
  }

  .lid-label {
    position: absolute; left: 650px; top: 350px;
    width: 480px; height: 480px; border-radius: 50%;
    background: var(--honey-deep); padding: 18px;
  }
  .lid-label__face {
    position: relative; width: 100%; height: 100%; border-radius: 50%;
    background: var(--cream); overflow: hidden;
    border: 3px solid var(--olive);
  }
  .lid-label__tagline {
    position: absolute; top: 92px; width: 100%; text-align: center;
    font-family: "Lobster", cursive; font-size: 34px; color: var(--olive);
    transform: rotate(-8deg);
  }
  .lid-label__name {
    position: absolute; top: 158px; width: 100%; text-align: center;
    font-family: "Lobster", cursive; font-size: 54px; color: var(--amber);
    transform: rotate(-10deg); z-index: 2;
  }
  .honey-pool {
    position: absolute; left: 0; bottom: 0; width: 100%; height: 48%;
    background: linear-gradient(180deg, var(--honey-light) 0%, var(--honey) 50%, var(--honey-deep) 100%);
    border-radius: 40% 60% 0 0 / 18% 22% 0 0;
  }
</style>
</head>
<body>

  <section class="front-label">
    <svg class="honey-band honey-band--top" viewBox="0 0 520 70" preserveAspectRatio="none">
      <path d="M0 0 H520 V30 C430 60 330 20 240 38 C150 56 70 30 0 44 Z" fill="var(--honey)"/>
      <path d="M280 46 C360 38 440 30 520 22 V30 C450 44 370 48 280 46 Z" fill="var(--honey-deep)"/>
    </svg>

    <div class="tree-art" role="img" aria-label="Illustration of a cypress tree draped in Spanish moss"></div>

    <div class="raw-badge">
      <div class="raw-badge__pct">100%</div>
      <div class="raw-badge__tag">RAW HONEY</div>
    </div>

    <h1 class="product-name">Ridgeway Amber</h1>

    <p class="infant-notice">Not recommended for infants under 1yrs of age</p>
    <p class="net-weight">16oz.</p>

    <svg class="honey-band honey-band--bottom" viewBox="0 0 520 70" preserveAspectRatio="none">
      <path d="M0 30 C90 14 170 36 260 24 C350 12 440 30 520 20 V70 H0 Z" fill="var(--honey)"/>
      <path d="M0 30 C90 14 170 36 260 24 C200 34 100 30 0 40 Z" fill="var(--honey-deep)"/>
    </svg>
  </section>

  <section class="lid-label">
    <div class="lid-label__face">
      <p class="lid-label__tagline">100% Raw Honey</p>
      <h2 class="lid-label__name">Ridgeway Amber</h2>
      <div class="honey-pool" role="img" aria-label="Illustration of flowing honey over honeycomb"></div>
    </div>
  </section>

</body>
</html>
```